Business Card Design Project

A business card for a new company in Ontario Canada called Build for Growth. It is a consulting company which uses Brixo as the medium for facilitation.

The target market is for senior leaders in healthcare and social services.

Industry/Entity Type

Healthcare

Requirements
Must have
• The name Build For Growth
Dana Montreuil RRT, B Ed (AD ed).
Tacticraft Facililitator (R)

Tag Line
Engaging Transforming and Innovative
The attached logo

danamontreuil@examplemail.com
416-555-0147
Should not have
• Lime green
Times New Roman or Arial font
Do not include Brixo bricks on the card.

```html
<!DOCTYPE html>
<html lang="en">
<head>
<meta charset="utf-8">
<title>Build for Growth — Business Card Set</title>
<link rel="stylesheet" href="https://fonts.googleapis.com/css2?family=Comic+Neue:wght@700&family=Mulish:wght@300;400;700;800&display=swap">
<style>
  :root {
    --paper: #ffffff;
    --ink: #111111;
    --edge: #1a1a1a;
    --orange: #ee5423;
    --purple: #6b2c91;
    --grey: #7a7a7a;
    --mark: #6b2c91;
    --display: "Comic Neue", "Comic Sans MS", cursive;
    --body: "Mulish", "Century Gothic", sans-serif;
  }
  * { box-sizing: border-box; margin: 0; padding: 0; }
  html, body { width: 848px; height: 1200px; overflow: hidden; background: var(--paper); }
  .sheet { position: relative; width: 848px; height: 1200px; }

  .card {
    position: absolute;
    background: var(--paper);
    border: 1.4px solid var(--edge);
    overflow: hidden;
  }
  .wordmark {
    font-family: var(--display);
    font-weight: 700;
    text-transform: uppercase;
    letter-spacing: 0.5px;
    white-space: nowrap;
  }
  .brand-dot { position: absolute; border-radius: 50%; background: var(--mark); }

  /* Card 1 — logo front */
  .card--front { left: 202px; top: 52px; width: 424px; height: 242px; }
  .card--front .brand-dot { left: 167px; top: 38px; width: 90px; height: 90px; }
  .card--front .wordmark {
    position: absolute; left: 0; right: 0; top: 150px;
    text-align: center; font-size: 17px; color: var(--ink);
  }

  /* Card 2 — orange back */
  .card--orange { left: 202px; top: 311px; width: 424px; height: 240px; text-align: center; }
  .card--orange .header { height: 73px; background: var(--paper); padding-top: 12px; }
  .card--orange .header .wordmark { font-size: 29px; color: var(--orange); line-height: 1; }
  .tagline {
    font-family: var(--body); font-weight: 800; text-transform: uppercase;
    font-size: 10.5px; letter-spacing: 0.2px;
  }
  .card--orange .tagline { color: var(--orange); margin-top: 6px; }
  .card--orange .panel { height: 167px; background: var(--orange); color: #fff; padding-top: 22px; }
  .person { font-family: var(--body); font-weight: 800; font-size: 18px; }
  .credentials { font-size: 6px; font-weight: 400; }
  .role { font-family: var(--body); font-weight: 400; font-size: 12.5px; }
  .card--orange .role { margin-top: 6px; }
  .card--orange .phone { font-family: var(--body); font-weight: 800; font-size: 15px; margin-top: 28px; }
  .card--orange .email { font-family: var(--body); font-weight: 300; font-size: 15px; margin-top: 20px; }

  /* Card 3 — vertical front */
  .card--tall { left: 44px; top: 698px; width: 243px; height: 423px; }
  .card--tall .brand-dot { left: 56px; top: 92px; width: 130px; height: 130px; }
  .card--tall .wordmark {
    position: absolute; left: 0; right: 0; top: 310px;
    text-align: center; font-size: 19px; color: var(--ink);
  }

  /* Card 4 — white back */
  .card--white { left: 358px; top: 786px; width: 424px; height: 240px; }
  .card--white .brand-dot { left: 12px; top: 17px; width: 36px; height: 36px; }
  .card--white .heading { position: absolute; left: 62px; top: 16px; }
  .card--white .heading .wordmark { font-size: 20px; color: var(--purple); line-height: 1; }
  .card--white .tagline { font-size: 7px; color: var(--grey); font-weight: 700; margin-top: 3px; }
  .card--white .identity { position: absolute; left: 0; right: 0; top: 96px; text-align: center; }
  .card--white .person { color: var(--purple); font-size: 19px; }
  .card--white .role { color: var(--grey); font-size: 13px; margin-top: 6px; }
  .card--white .contact { position: absolute; right: 12px; top: 184px; text-align: right; font-family: var(--body); color: var(--ink); }
  .card--white .phone { font-weight: 800; font-size: 16px; }
  .card--white .email { font-weight: 400; font-size: 13.5px; margin-top: 4px; }
</style>
</head>
<body>
<main class="sheet">

  <section class="card card--front" aria-label="Card front">
    <span class="brand-dot"></span>
    <p class="wordmark">Build for Growth</p>
  </section>

  <section class="card card--orange" aria-label="Card back, orange">
    <header class="header">
      <h1 class="wordmark">Build for Growth</h1>
      <p class="tagline">Engaging Transforming and Innovative</p>
    </header>
    <div class="panel">
      <p class="person">Dana Montreuil <span class="credentials">RRT, BA (AD ed).</span></p>
      <p class="role">Tacticraft Facilillitator (R)</p>
      <p class="phone">416-555-0147</p>
      <p class="email">danamontreuil@examplemail.com</p>
    </div>
  </section>

  <section class="card card--tall" aria-label="Vertical card front">
    <span class="brand-dot"></span>
    <p class="wordmark">Build for Growth</p>
  </section>

  <section class="card card--white" aria-label="Card back, white">
    <span class="brand-dot"></span>
    <div class="heading">
      <h2 class="wordmark">Build for Growth</h2>
      <p class="tagline">Engaging Transforming and Innovative</p>
    </div>
    <div class="identity">
      <p class="person">Dana Montreuil <span class="credentials">RRT, BA (AD ed).</span></p>
      <p class="role">Tacticraft Facilillitator (R)</p>
    </div>
    <div class="contact">
      <p class="phone">416-555-0147</p>
      <p class="email">danamontreuil@examplemail.com</p>
    </div>
  </section>

</main>
</body>
</html>
```